Zanquorra Business Card Design

Zanquorra is a small and new restaurant/ bar location in Hong Kong. The name "Djibouti" derives from an African country. There is no specific reason behind other than the fact, that the bar is somewhat inspired by African elements (only inspired but not purely based on African cuisine etc.).

The bar is somewhat a fusion of African, Mediterranean and Oriental (Old French Vietnam) elements.

However, it is very imperative to stress, that the overall look and feel of Zanquorra is a very high end cocktail lounge/ bar location. The bar is tucked away in a hidden alley, so people will have to know about it. The idea is to send the consumer off in an Escape or hidden remote location where they are at ease in a hip, stylish and trendy environment.

The card needs to feel high-end.

Final logo artwork has been attached and also pictures of the bar/ restaurant itself. The logo ie monkey head cannot be modified. However, the background color and the color of the type "ZANQUORRA" can be changed.

The following details need to fit onto the business card. Of course they can be arranged to your liking:

LOGO

Colin Vey
Partner

+852 97035164
xxx@zanquorra.com
www.zanquorra.com
7C, Brennick Road, Wan Chai, Hong Kong

```html
<!DOCTYPE html>
<html lang="en">
<head>
<meta charset="utf-8">
<title>Zanquorra Business Card</title>
<link rel="stylesheet" href="https://fonts.googleapis.com/css2?family=Cinzel:wght@700&family=Roboto+Condensed:wght@400;700&display=swap">
<style>
  :root {
    --page: #ececec;
    --card: #ffffff;
    --ink: #1e1512;
    --accent-red: #d81f1f;
    --photo-dark: #1c1210;
    --photo-warm: #4a2a1c;
    --name-blue: #2a63b3;
    --icon-gold: #9a6a2c;
    --text: #222222;
  }
  html, body {
    margin: 0;
    width: 1200px;
    height: 977px;
    overflow: hidden;
    background: var(--page);
  }
  .card {
    position: absolute;
    left: 240px;
    width: 720px;
    height: 412px;
    background: var(--card);
    box-shadow: 0 4px 18px rgba(0,0,0,0.12);
  }
  .card--front { top: 46px; }
  .card--back { top: 519px; }
  .card svg { display: block; }
  .wordmark {
    font-family: "Cinzel", serif;
    font-weight: 700;
    fill: var(--ink);
    letter-spacing: 2px;
  }
  .site-url {
    font-family: "Roboto Condensed", sans-serif;
    font-size: 17px;
    fill: #e8e2dc;
  }
  .holder-name, .holder-role {
    font-family: "Roboto Condensed", sans-serif;
    font-weight: 700;
    font-size: 24px;
    fill: var(--name-blue);
  }
  .contact-line {
    font-family: "Roboto Condensed", sans-serif;
    font-size: 19px;
    fill: var(--text);
  }
  .icon-dot { fill: var(--icon-gold); }
  .icon-glyph { fill: none; stroke: #fff; stroke-width: 1.6; }
</style>
</head>
<body>

<div class="card card--front">
  <svg width="720" height="412" viewBox="0 0 720 412">
    <defs>
      <linearGradient id="venueTone" x1="0" y1="0" x2="1" y2="1">
        <stop offset="0" stop-color="var(--photo-dark)"/>
        <stop offset="0.55" stop-color="var(--photo-warm)"/>
        <stop offset="1" stop-color="#2a1a14"/>
      </linearGradient>
    </defs>
    <path class="venue-photo" role="img" aria-label="Photo of the dimly lit cocktail lounge interior with lanterns and purple seating"
          d="M320 0 Q560 120 590 412 L720 412 L720 0 Z" fill="url(#venueTone)"/>
    <path d="M320 0 Q560 120 590 412" fill="none" stroke="var(--accent-red)" stroke-width="4"/>
    <text class="site-url" x="690" y="36" text-anchor="end">www.zanquorra.com</text>
    <circle cx="190" cy="150" r="75" fill="var(--ink)"/>
    <text class="wordmark" x="190" y="300" font-size="40" text-anchor="middle">ZANQUORRA</text>
  </svg>
</div>

<div class="card card--back">
  <svg width="720" height="412" viewBox="0 0 720 412">
    <circle cx="220" cy="160" r="80" fill="var(--ink)"/>
    <text class="wordmark" x="220" y="320" font-size="42" text-anchor="middle">ZANQUORRA</text>

    <text class="holder-name" x="430" y="92">Colin Vey</text>
    <text class="holder-role" x="430" y="122">Partner</text>

    <g class="contact-row">
      <circle class="icon-dot" cx="440" cy="170" r="10"/>
      <rect class="icon-glyph" x="436" y="163" width="8" height="14" rx="1.5"/>
      <text class="contact-line" x="460" y="177">+852 97035164</text>
    </g>
    <g class="contact-row">
      <circle class="icon-dot" cx="440" cy="206" r="10"/>
      <rect class="icon-glyph" x="434" y="201" width="12" height="9"/>
      <path class="icon-glyph" d="M434 201 L440 206 L446 201"/>
      <text class="contact-line" x="460" y="213">xxx@zanquorra.com</text>
    </g>
    <g class="contact-row">
      <circle class="icon-dot" cx="440" cy="242" r="10"/>
      <circle class="icon-glyph" cx="440" cy="242" r="6"/>
      <path class="icon-glyph" d="M434 242 H446 M440 236 V248"/>
      <text class="contact-line" x="460" y="249">www.zanquorra.com</text>
    </g>
    <g class="contact-row">
      <circle class="icon-dot" cx="440" cy="278" r="10"/>
      <path class="icon-glyph" d="M440 285 C436 280 435 277 435 275 A5 5 0 0 1 445 275 C445 277 444 280 440 285 Z"/>
      <text class="contact-line" x="460" y="285">7C, Brennick Road,</text>
      <text class="contact-line" x="460" y="309">Wan Chai, Hong Kong</text>
    </g>
  </svg>
</div>

</body>
</html>
```